Tervolan Pty Ltd professional business card

A professional business card template using the colours from the supplied logo.
Clean crisp lines while, Modern while not being over the top.

Target Market(s)

Construction, commerical and industrial

Industry/Entity Type

Communications

Contact Information for Business Card

For a Communications, IT, Optical fibre installation company

Colors
37b8a4

```html
<!DOCTYPE html>
<html lang="en">
<head>
<meta charset="utf-8">
<title>Tervolan Pty Ltd – Business Card</title>
<link rel="stylesheet" href="https://fonts.googleapis.com/css2?family=Montserrat:wght@600;700&family=Josefin+Sans:wght@400;600&display=swap">
<style>
  :root {
    --stage: #1f1f20;
    --card: #101112;
    --teal: #2fa3b3;
    --silver: #c9cacb;
    --grey: #8b8c8e;
    --text: #bdbec0;
    --divider: #5a5b5d;
  }
  * { box-sizing: border-box; margin: 0; padding: 0; }
  html, body {
    width: 1200px; height: 900px; overflow: hidden;
    background: radial-gradient(ellipse at 60% 40%, #2c2c2d 0%, var(--stage) 70%);
  }
  .sheet {
    position: relative; width: 1200px; height: 900px;
    display: flex; flex-direction: column; align-items: center; justify-content: center; gap: 40px;
  }
  .card {
    position: relative; width: 720px; height: 400px;
    background: var(--card);
    border-left: 3px solid var(--teal);
    border-bottom: 3px solid var(--teal);
    box-shadow: 0 18px 40px rgba(0,0,0,.55);
    overflow: hidden;
  }
  .wordmark {
    font-family: "Montserrat", sans-serif; font-weight: 700;
    letter-spacing: 2px; text-transform: uppercase;
  }
  .card-front { display: flex; align-items: center; justify-content: center; }
  .card-front .wordmark { font-size: 64px; color: var(--silver); }

  .card-back { display: flex; align-items: center; padding: 0 50px 0 60px; }
  .card-back .wordmark { font-size: 46px; color: var(--grey); width: 300px; }
  .divider { width: 2px; height: 230px; background: var(--divider); margin: 0 34px 0 20px; }
  .contact { font-family: "Josefin Sans", sans-serif; color: var(--text); }
  .contact-name { font-weight: 600; font-size: 24px; color: var(--teal); text-transform: uppercase; letter-spacing: .5px; }
  .contact-role { font-size: 20px; color: var(--grey); margin-bottom: 20px; }
  .contact-line { display: flex; align-items: center; gap: 10px; font-size: 19px; line-height: 30px; }
  .contact-line svg { width: 18px; height: 18px; flex: none; }
  .accent { color: var(--teal); }
  .address { font-size: 19px; margin-top: 16px; line-height: 30px; }
  .social-mark { width: 16px; height: 16px; border: 2px solid var(--teal); border-radius: 4px; flex: none; margin: 0 1px; }
</style>
</head>
<body>
<main class="sheet">
  <section class="card card-front">
    <span class="wordmark">Tervolan</span>
  </section>

  <section class="card card-back">
    <span class="wordmark">Tervolan</span>
    <div class="divider"></div>
    <div class="contact">
      <p class="contact-name">Marcus Ellery</p>
      <p class="contact-role">Project Manager</p>
      <p class="contact-line">
        <svg viewBox="0 0 24 24" fill="none" stroke="#2fa3b3" stroke-width="2"><path d="M5 3h4l2 5-3 2a11 11 0 0 0 6 6l2-3 5 2v4a2 2 0 0 1-2 2A17 17 0 0 1 3 5a2 2 0 0 1 2-2z"/></svg>
        555 014 2738
      </p>
      <p class="contact-line">
        <svg viewBox="0 0 24 24" fill="none" stroke="#2fa3b3" stroke-width="2"><rect x="2" y="5" width="20" height="14" rx="1"/><path d="M2 6l10 7 10-7"/></svg>
        marcus@tervolanptyltd.com
      </p>
      <p class="contact-line">
        <svg viewBox="0 0 24 24" fill="none" stroke="#2fa3b3" stroke-width="2"><circle cx="12" cy="12" r="10"/><path d="M2 12h20M12 2c3 3 3 17 0 20M12 2c-3 3-3 17 0 20"/></svg>
        <span>www.<span class="accent">tervolanptyltd</span>.com</span>
      </p>
      <p class="address">PoBox 481930, Sydney, AU</p>
      <p class="contact-line">
        <span class="social-mark"></span>
        @brightlinecrew
      </p>
    </div>
  </section>
</main>
</body>
</html>
```